WordPress Design - dental products

We need a Wordpress theme for a company based in Mexico, USA and Europe. We sell orthodontic products for dental industry. We are very compromised with our customers and all our products are the better option in the market. The Quality and image are really important for us.

The idea is to have a Wordpress Website that we can manage, and our customers can get info from us. Our corporate image is based in innovation, quality and customer service.

the general idea is to have a wordpress site to manage all the info and the store is in a different system, so that we need is the wordpress site desing for the frontend. 

We will need more designs so in the future for our website, so the winner will help us for many projects.

So we hope the best design.
Updates

Hi, this "wordpress site" will be used as a homepage, the eCommerce is independent. So the design is related to corporate site. Thank you

Target Market(s)

Target: dental and orthodontic industry, academy and general customers. Private an public organizations related to medical and dental industry.
Investigators and press

Industry/Entity Type

Dental

Requirements
Must have
• Must Have Priorities:
• - Respect the logo (included)
• - Respect colors (actual website)
• - Modern style and innovated website
Nice to have
• Be funcionality, simply and easy to use, think about user interfaze (UI)
Should not have
• The design should not use old-style, serif fonts like Times New Roman. Not use cartoons, flash animations, free icons. Don't modify the logo.

```html
<!DOCTYPE html>
<html lang="en">
<head>
<meta charset="utf-8">
<title>Orto-Vela – Dental Care</title>
<link href="https://fonts.googleapis.com/css2?family=Ubuntu:wght@400;500;700&family=Yanone+Kaffeesatz:wght@400;600&family=Roboto:wght@400;700&display=swap" rel="stylesheet">
<style>
:root{
  --maroon-dark:#4b0e1b;
  --maroon:#8d1a30;
  --maroon-line:#b34a5d;
  --panel:#e8e6e3;
  --ink:#2b2b2b;
  --orange:#e09a2c;
  --tan:#d9b48a;
  --footer:#141d26;
  --footer-text:#c9a66b;
}
*{box-sizing:border-box;margin:0;padding:0}
html,body{width:887px;height:1200px;overflow:hidden;background:#fff}
body{position:relative;font-family:"Roboto",Arial,sans-serif;color:var(--ink)}
.abs{position:absolute}

.site-header{left:0;top:0;width:887px;height:92px;background:var(--maroon-dark)}
.brand{left:43px;top:6px;display:flex;align-items:center;gap:10px}
.brand-mark{width:54px;height:78px;border:2px solid var(--tan)}
.brand-name{font-family:"Ubuntu",sans-serif;font-weight:700;font-size:30px;color:#fff}
.header-call{right:16px;top:22px;text-align:right;font-family:"Yanone Kaffeesatz",sans-serif;line-height:1}
.header-call .label{color:var(--tan);font-size:28px;font-weight:600}
.header-call .number{color:#fff;font-size:30px;font-weight:600;margin-top:2px}

.hero-band{left:0;top:92px;width:887px;height:283px;background:var(--maroon)}
.hero-shadow{left:30px;top:420px;width:827px;height:22px;border-radius:50%;background:rgba(0,0,0,.55);filter:blur(9px)}
.hero-panel{left:17px;top:111px;width:852px;height:321px;background:var(--panel)}

.main-nav{left:36px;top:126px;width:230px;height:288px;background:var(--maroon);border:3px solid #a8485a;padding:6px}
.main-nav ul{list-style:none;border:2px solid #b65a6b;height:100%;padding:4px 8px 0}
.main-nav li{font-family:"Ubuntu",sans-serif;font-size:15px;color:#fff;height:28.3px;line-height:28px;padding-left:12px;border-bottom:2px solid var(--maroon-line)}
.main-nav li:first-child{color:#2a0a10}
.main-nav li:last-child{border-bottom:none}

.photo{background:#fff;padding:7px;box-shadow:0 2px 6px rgba(0,0,0,.3)}
.photo .fill{width:100%;height:100%}
.photo-left{left:285px;top:178px;width:140px;height:190px;transform:rotate(-9deg)}
.photo-left .fill{background:linear-gradient(135deg,#d9dde2,#a6a09a 55%,#6a5a55)}
.photo-right{left:730px;top:172px;width:120px;height:190px;transform:rotate(8deg)}
.photo-right .fill{background:linear-gradient(135deg,#f2efe9,#d9c4b0 60%,#b8927a)}
.photo-main{left:398px;top:129px;width:353px;height:240px}
.photo-main .fill{background:linear-gradient(120deg,#cfd9df,#9fb9c6 40%,#e6c9a8 75%,#c39a6e)}
.hero-caption{left:282px;top:355px;width:568px;height:60px;background:var(--maroon-dark);color:#fff;font-family:"Ubuntu",sans-serif;font-size:19.5px;line-height:60px;padding-left:10px}

.side-title{left:34px;top:467px;width:208px;height:39px;background:var(--maroon-dark);color:#fff;font-family:"Ubuntu",sans-serif;font-size:15px;text-align:center;line-height:39px}
.side-list{left:37px;top:506px;width:202px;height:582px;background:var(--maroon);border:2px solid #a8485a;border-top:none;list-style:none;padding:10px 12px 0}
.side-list li{height:28.3px;line-height:27px;font-size:10.5px;font-weight:700;color:#f3d7dc;padding-left:10px;border-bottom:2px solid var(--maroon-line)}
.side-list li:last-child{border-bottom:none}

.welcome{left:261px;top:474px;width:608px;height:38px;border-bottom:1px dashed #9a9a9a;font-family:"Ubuntu",sans-serif;font-size:25px;color:#222}
.welcome .name{font-family:"Yanone Kaffeesatz",sans-serif;font-weight:600;font-size:34px;color:var(--orange);margin-left:4px}
.copy{font-size:10.6px;line-height:16px;color:#333}
.copy p{margin-bottom:12px}
.copy-narrow{left:263px;top:525px;width:330px}
.copy-wide{left:266px;top:731px;width:600px}
.welcome-photo{left:592px;top:526px;width:278px;height:185px;padding:7px}
.welcome-photo .fill{background:linear-gradient(120deg,#e7ecf0,#b9c7d1 45%,#8d7a6c 75%,#5a4035)}
.divider{left:261px;top:918px;width:608px;border-top:1px dashed #9a9a9a}

.feature-title{top:941px;font-family:"Ubuntu",sans-serif;font-size:17px;color:#333}
.feature{top:975px;width:191px;height:112px;border:1px solid #c9cfd4;border-radius:6px;padding:4px;background:#f4f6f8}
.feature .fill{width:100%;height:100%;border-radius:3px;position:relative}
.feature-call .fill{background:linear-gradient(120deg,#dfe6ec,#b7c6d2 50%,#9a7a66)}
.feature-implants .fill{background:linear-gradient(120deg,#eee7e2,#d7b7ae 50%,#c6c1bd)}
.feature-team .fill{background:linear-gradient(120deg,#e9eef2,#c5d2db 50%,#a3b3c0)}
.feature-label{position:absolute;left:0;right:0;bottom:6px;text-align:center;font-family:"Ubuntu",sans-serif;font-size:17px;color:#fff;text-shadow:0 1px 2px rgba(0,0,0,.7)}
.feature-call .feature-label{font-size:25px;bottom:4px}
.feature-label svg{vertical-align:-4px;margin-left:4px}

.site-footer{left:0;top:1130px;width:887px;height:70px;background:var(--footer);font-family:"Ubuntu",sans-serif;font-size:9.5px;color:var(--footer-text);text-align:center;line-height:70px;word-spacing:1px}
.site-footer span{margin:0 6px;color:#9c8a6a}
</style>
</head>
<body>
<header class="site-header abs">
  <div class="brand abs"><div class="brand-mark"></div><div class="brand-name">Orto-Vela</div></div>
  <div class="header-call abs"><div class="label">Call Us</div><div class="number">555.0142.7788</div></div>
</header>

<div class="hero-band abs"></div>
<div class="hero-shadow abs"></div>
<section class="hero-panel abs"></section>

<nav class="main-nav abs">
  <ul>
    <li>Home</li><li>About Us</li><li>Our Practice</li><li>Procedures</li><li>Our Mission</li>
    <li>Dental Implants</li><li>FAQs</li><li>Smile Gallery</li><li>Contact Us</li>
  </ul>
</nav>

<div class="photo photo-left abs"><div class="fill" role="img" aria-label="Dental assistant with mask at work"></div></div>
<div class="photo photo-right abs"><div class="fill" role="img" aria-label="Relaxed patient in dental chair"></div></div>
<div class="photo photo-main abs"><div class="fill" role="img" aria-label="Smiling dental hygienist showing floss to a patient"></div></div>
<div class="hero-caption abs">High quality Dental Care in A Comfortable, Caring Environment</div>

<div class="side-title abs">Left Panel</div>
<ul class="side-list abs">
  <li>lorem ipsum dolor sit amet</li><li>lorem ipsum dolor sit amet</li><li>lorem ipsum dolor sit amet</li><li>lorem ipsum dolor sit amet</li>
  <li>lorem ipsum dolor sit amet</li><li>lorem ipsum dolor sit amet</li><li>lorem ipsum dolor sit amet</li><li>lorem ipsum dolor sit amet</li>
  <li>lorem ipsum dolor sit amet</li><li>lorem ipsum dolor sit amet</li><li>lorem ipsum dolor sit amet</li><li>lorem ipsum dolor sit amet</li>
  <li>lorem ipsum dolor sit amet</li><li>lorem ipsum dolor sit amet</li><li>lorem ipsum dolor sit amet</li><li>lorem ipsum dolor sit amet</li>
  <li>lorem ipsum dolor sit amet</li><li>lorem ipsum dolor sit amet</li><li>lorem ipsum dolor sit amet</li><li>lorem ipsum dolor sit amet</li>
</ul>

<h1 class="welcome abs">welcome to <span class="name">Orto-Vela</span></h1>

<div class="copy copy-narrow abs">
  <p>"After 20 years of teaching dentists how to refine their technique and many years of writing textbooks, I currently devote my time to my office and the hands-on practice of dentistry. I'd like to welcome you personally to my dental practice, and I invite you to meet my highly experienced team of professionals.</p>
  <p>"We have offered complete dental care of the highest quality since 1978. We provide Preventive Services, Tooth Whitening and Cosmetic Dentistry for a beautiful smile, Endodontics (root canal treatment) to treat painful teeth, Sedation Dentistry so you can relax, and Dental Implants to restore what is missing. We offer total care.</p>
</div>
<div class="photo welcome-photo abs"><div class="fill" role="img" aria-label="Dentist talking with a patient in the treatment chair"></div></div>

<div class="copy copy-wide abs">
  <p>"Our approach to your health is simple: We use our education, experience and dedication to provide every patient with superior dental care.</p>
  <p>"This passion for excellence is not just a goal, but a standard every member of our team holds.</p>
  <p>"We also pride ourselves with our state of the art procedures, training and technology. This includes creating a beautiful smile using techniques that preserve as much of the original tooth as possible.</p>
  <p>"Our abilities are renowned throughout the dental profession and I hope if you have any questions you will contact us by an e-mail note, by phone or just by dropping by."</p>
</div>

<div class="divider abs"></div>

<h2 class="feature-title abs" style="left:261px">Call Us</h2>
<h2 class="feature-title abs" style="left:473px">Dental Implants</h2>
<h2 class="feature-title abs" style="left:682px">Meet The Dentists</h2>

<div class="feature feature-call abs" style="left:261px"><div class="fill" role="img" aria-label="Woman calling on the phone"><div class="feature-label">555.246.1300</div></div></div>
<div class="feature feature-implants abs" style="left:470px"><div class="fill" role="img" aria-label="Dental model with implants"><div class="feature-label">More Information<svg width="20" height="20" viewBox="0 0 20 20"><circle cx="10" cy="10" r="9" fill="#111" stroke="#fff" stroke-width="1.5"/><path d="M5 10h9M10 6l4 4-4 4" stroke="#fff" stroke-width="2" fill="none"/></svg></div></div></div>
<div class="feature feature-team abs" style="left:679px"><div class="fill" role="img" aria-label="Dental team members"><div class="feature-label">View List of Dentists</div></div></div>

<footer class="site-footer abs">© Copyright Orto-Vela<span>|</span>All Rights Reserved&nbsp; Home<span>|</span>About Us<span>|</span>Our Practice<span>|</span>Procedures<span>|</span>Our Mission<span>|</span>Dental Implants<span>|</span>FAQs<span>|</span>Smile Gallery<span>|</span>Contact Us</footer>
</body>
</html>
```